Telecommunication company needs a car wrap design for 3 vans

We are a telecommunication company called "Mirovan" based in Australia's capital city Canberra.
We have the logo, colour scheme, website (www.mirovan.com.au) and complete brand guidelines created. Now we need a design for two Kolbe Drifters LWB (one in white and one in grey colour) and one Brenoix Parcel LWB (also in white colour).
We would like a modern design which stands out as colours are very neutral and will look uniform on all cars. We preffer not to have fully wrapped car design but open for suggestions.
Please referr to attachments.

List of services:
- antenna and satellite
- tv wall mounting
- phone and data
- home theatre
- cabling contractor

Dear Participants, thank you for your designs, some of them were better than others. What we really liked was your creativity, however most of the designs would not be aplicable on the grey colour vehicle as the colours would not simply play together. Also many of the designs were missing services as a vital part of van signage. Please bear this in your mind. We are starting a new round of designs and will be very happy if you all will participate again and bring your ideas. Good luck to everyone. Kind Regards,

Telecommunications

• Logo on the bonet

Sides and rear must have logo, website, phone number, sevices

List of services:
- antenna and satellite
- tv wall mounting
- phone and data
- home theatre
- cabling contractor
• social media icons

```html
<!DOCTYPE html>
<html lang="en">
<head>
<meta charset="utf-8">
<title>Mirovan van livery – side elevations</title>
<link href="https://fonts.googleapis.com/css2?family=Open+Sans:wght@600;700&display=swap" rel="stylesheet">
<style>
  :root {
    --slate: #3a4150;
    --panel: #f3f3f3;
    --page: #ffffff;
    --trim: #2e2f31;
    --glass: #d8d9db;
    --rim: #c9cacc;
  }
  html, body {
    margin: 0;
    padding: 0;
    width: 1164px;
    height: 1200px;
    overflow: hidden;
    background: var(--page);
  }
  .sheet {
    position: relative;
    width: 1164px;
    height: 1200px;
  }
  .van-elevation {
    position: absolute;
    left: 0;
    width: 1164px;
    height: 560px;
  }
  .van-elevation--left { top: 20px; }
  .van-elevation--right { top: 600px; }
  .livery-text {
    font-family: "Open Sans", sans-serif;
    fill: var(--slate);
    font-weight: 600;
  }
  .brand-name { font-size: 92px; letter-spacing: 1px; }
  .web-address { font-size: 22px; }
  .phone-number { font-size: 24px; font-weight: 700; }
  .service-item { font-size: 13.5px; }
  .social-handle { font-size: 16px; }
  .body-panel { fill: var(--panel); }
  .wrap-band { fill: var(--slate); }
  .trim { fill: var(--trim); }
  .glass { fill: var(--glass); }
  .rim { fill: var(--rim); }
  .brand-dot { fill: var(--slate); }
</style>
</head>
<body>
<main class="sheet">

  <!-- Driver-side elevation -->
  <svg class="van-elevation van-elevation--left" viewBox="0 0 1164 560" role="img" aria-label="Mirovan livery on the left side of the van">
    <defs>
      <clipPath id="body-left">
        <path d="M10 400 L10 330 Q20 290 90 272 L225 150 Q300 102 480 100 L1065 100 Q1110 102 1120 140 L1128 420 Q1128 472 1100 476 L10 476 Z"/>
      </clipPath>
    </defs>
    <g class="vehicle">
      <path class="body-panel" d="M10 400 L10 330 Q20 290 90 272 L225 150 Q300 102 480 100 L1065 100 Q1110 102 1120 140 L1128 420 Q1128 472 1100 476 L10 476 Z"/>
      <g clip-path="url(#body-left)">
        <path class="wrap-band" d="M1080 100 L1164 100 L1164 500 L225 500 L225 378 L780 378 C830 378 870 374 905 364 C1030 330 1062 220 1080 100 Z"/>
        <rect class="trim" x="0" y="380" width="120" height="100"/>
        <rect class="trim" x="1090" y="100" width="80" height="400"/>
        <rect class="trim" x="270" y="425" width="720" height="40"/>
      </g>
      <path class="glass" d="M255 205 L330 128 Q400 118 460 120 L460 245 L270 262 Z"/>
      <circle class="trim" cx="165" cy="462" r="62"/>
      <circle class="rim" cx="165" cy="462" r="38"/>
      <circle class="trim" cx="955" cy="462" r="62"/>
      <circle class="rim" cx="955" cy="462" r="38"/>
    </g>

    <text class="livery-text phone-number" x="272" y="333">1300 555 014</text>

    <circle class="brand-dot" cx="524" cy="148" r="9"/>
    <text class="livery-text social-handle" x="540" y="154">@mirovan</text>

    <circle class="brand-dot" cx="748" cy="190" r="52"/>
    <text class="livery-text brand-name" x="748" y="318" text-anchor="middle">mirovan</text>
    <text class="livery-text web-address" x="748" y="360" text-anchor="middle">mirovan.com.au</text>

    <g class="service-list">
      <circle class="brand-dot" cx="886" cy="142" r="5"/>
      <text class="livery-text service-item" x="896" y="147">Antenna &amp; Satellite</text>
      <circle class="brand-dot" cx="886" cy="160" r="5"/>
      <text class="livery-text service-item" x="896" y="165">TV wall mounting</text>
      <circle class="brand-dot" cx="886" cy="177" r="5"/>
      <text class="livery-text service-item" x="896" y="182">Phone &amp; Data</text>
      <circle class="brand-dot" cx="886" cy="194" r="5"/>
      <text class="livery-text service-item" x="896" y="199">Home Theatre</text>
      <circle class="brand-dot" cx="886" cy="211" r="5"/>
      <text class="livery-text service-item" x="896" y="216">Cabling contractor</text>
    </g>
  </svg>

  <!-- Passenger-side elevation -->
  <svg class="van-elevation van-elevation--right" viewBox="0 0 1164 560" role="img" aria-label="Mirovan livery on the right side of the van">
    <defs>
      <clipPath id="body-right">
        <path transform="translate(1164 0) scale(-1 1)" d="M10 400 L10 330 Q20 290 90 272 L225 150 Q300 102 480 100 L1065 100 Q1110 102 1120 140 L1128 420 Q1128 472 1100 476 L10 476 Z"/>
      </clipPath>
    </defs>
    <g class="vehicle">
      <path class="body-panel" transform="translate(1164 0) scale(-1 1)" d="M10 400 L10 330 Q20 290 90 272 L225 150 Q300 102 480 100 L1065 100 Q1110 102 1120 140 L1128 420 Q1128 472 1100 476 L10 476 Z"/>
      <g clip-path="url(#body-right)">
        <g transform="translate(1164 0) scale(-1 1)">
          <path class="wrap-band" d="M1080 100 L1164 100 L1164 500 L225 500 L225 378 L780 378 C830 378 870 374 905 364 C1030 330 1062 220 1080 100 Z"/>
          <rect class="trim" x="0" y="380" width="120" height="100"/>
          <rect class="trim" x="1090" y="100" width="80" height="400"/>
          <rect class="trim" x="270" y="425" width="720" height="40"/>
        </g>
      </g>
      <path class="glass" transform="translate(1164 0) scale(-1 1)" d="M255 205 L330 128 Q400 118 460 120 L460 245 L270 262 Z"/>
      <circle class="trim" cx="999" cy="462" r="62"/>
      <circle class="rim" cx="999" cy="462" r="38"/>
      <circle class="trim" cx="209" cy="462" r="62"/>
      <circle class="rim" cx="209" cy="462" r="38"/>
    </g>

    <g class="service-list">
      <circle class="brand-dot" cx="159" cy="142" r="5"/>
      <text class="livery-text service-item" x="169" y="147">Antenna &amp; Satellite</text>
      <circle class="brand-dot" cx="159" cy="160" r="5"/>
      <text class="livery-text service-item" x="169" y="165">TV wall mounting</text>
      <circle class="brand-dot" cx="159" cy="177" r="5"/>
      <text class="livery-text service-item" x="169" y="182">Phone &amp; Data</text>
      <circle class="brand-dot" cx="159" cy="194" r="5"/>
      <text class="livery-text service-item" x="169" y="199">Home Theatre</text>
      <circle class="brand-dot" cx="159" cy="211" r="5"/>
      <text class="livery-text service-item" x="169" y="216">Cabling contractor</text>
    </g>

    <circle class="brand-dot" cx="574" cy="148" r="9"/>
    <text class="livery-text social-handle" x="590" y="154">@mirovan</text>

    <circle class="brand-dot" cx="425" cy="190" r="52"/>
    <text class="livery-text brand-name" x="425" y="318" text-anchor="middle">mirovan</text>
    <text class="livery-text web-address" x="425" y="360" text-anchor="middle">mirovan.com.au</text>

    <text class="livery-text phone-number" x="737" y="333">1300 555 014</text>
  </svg>

</main>
</body>
</html>
```